We need to a website for a contact center that provides answering services by voice and chat.

A similar website in terms of design is the following site:
http://www.brindlecallhub.net/

The colors and look and feel should be different and creative but the structure should be similar to the above mentioned website.

Attached is the text file.

The design should communicate professionalism and friendly customer service oriented company. The visitor to the site must have a feel that "this company looks professional and they will take care of my client."

I am looking for design only, but if the designer will also do the coding, it will be an advantage.

Target Market(s)

Our target market are lawyers and doctors who require someone to answer their clients calls 24/7.

Industry/Entity Type

It Company

Requirements
Nice to have
• Since the company is based in Dubai, the website should reflect the Middle East people not pure European or pure Asians. A mixture of nationalities is fine to be visible in the pictures but it must include at least an arab or middle eastern person.
Should not have
• No old style, Times Roman font, do not include illustrations or cartoon graphics or pictures that are very common or widely used.

```html
<!DOCTYPE html>
<html lang="en">
<head>
<meta charset="utf-8">
<title>Kernel Group – Call Center &amp; Live Answering</title>
<link rel="stylesheet" href="https://fonts.googleapis.com/css2?family=Ubuntu:wght@400;500&family=Bebas+Neue&display=swap">
<style>
:root{
  --navy:#003a5c;
  --navy-deep:#002b45;
  --blue:#0b7fc0;
  --sky:#2aa0d8;
  --ink:#1d1d1d;
  --text:#333;
  --panel:#f1f1f1;
  --line:#d3d3d3;
  --green:#2aa61c;
  --page:#ffffff;
}
*{box-sizing:border-box;margin:0;padding:0}
html,body{width:1029px;height:1200px;overflow:hidden}
body{position:relative;background:var(--page);font-family:"Ubuntu",sans-serif;color:var(--text);font-size:11px}
.topband{position:absolute;left:0;top:0;width:1029px;height:63px;background:var(--navy)}
.toplinks{position:absolute;right:75px;top:11px;color:#fff;font-size:11.5px;display:flex;gap:8px;align-items:center}
.toplinks .chat-dot{display:inline-block;width:18px;height:13px;border-radius:50%;background:#f5c400;margin-right:3px;vertical-align:-2px}
.sheet{position:absolute;left:103px;top:38px;width:823px;height:1145px;background:#fff;border-radius:6px;box-shadow:0 0 4px rgba(0,0,0,.25)}
.brand{position:absolute;left:19px;top:30px;font-size:28px;letter-spacing:1px;color:var(--ink);line-height:1}
.brand small{display:block;font-size:12px;letter-spacing:8px;margin-top:4px;color:var(--ink)}
.search{position:absolute;left:609px;top:11px;width:206px;height:25px;border:1px solid #ccc;border-radius:3px;background:#eee;font-size:10px;font-style:italic;color:#888;padding:7px 9px}
.search .btn{position:absolute;right:-1px;top:-1px;width:33px;height:25px;background:#222;border-radius:0 3px 3px 0}
.callus{position:absolute;right:9px;top:50px;font-size:17px;color:var(--ink);display:flex;align-items:center;gap:6px}
.callus b{font-weight:400;color:var(--blue)}
.nav{position:absolute;left:0;top:84px;width:823px;height:41px;background:linear-gradient(#0a4f7a,var(--navy));display:flex;justify-content:space-between;padding:0 19px 0 19px;align-items:center}
.nav a{color:#fff;font-size:11.5px;text-decoration:none;letter-spacing:.3px}
.hero{position:absolute;left:9px;top:135px;width:805px;height:321px;border:2px solid #ddd;border-radius:3px;background:linear-gradient(100deg,#6b5040 0%,#b59079 30%,#d9c8b8 55%,#c7c0b6 100%)}
.trial{position:absolute;left:544px;top:29px;width:230px;height:233px;background:rgba(240,240,240,.92);border-radius:4px;padding:9px 13px}
.trial h2{font-family:"Bebas Neue",sans-serif;font-weight:400;color:var(--sky);font-size:44px;line-height:1;margin-bottom:5px}
.trial .field{height:29px;border:2px solid #ccc;border-radius:4px;background:#fff;margin-bottom:8px;font-size:11px;font-style:italic;color:#777;padding:6px 12px}
.trial .go{position:absolute;right:17px;top:175px;width:103px;height:35px;background:var(--green);color:#fff;border-radius:3px;font-size:13px;letter-spacing:.5px;text-align:center;line-height:35px}
.dots{position:absolute;left:346px;top:288px;display:flex;gap:5px}
.dots i{width:18px;height:18px;border-radius:50%;background:#fff}
.dots i:first-child{background:var(--blue)}
.side{position:absolute;left:9px;width:245px;background:linear-gradient(#f4f4f4,#fff);border:1px solid var(--line);border-radius:3px}
.side h3{font-weight:400;color:var(--navy);font-size:18px;position:absolute;left:52px;top:11px}
.side p{position:absolute;left:53px;top:37px;width:185px;font-size:10.5px;line-height:17px;color:#333}
.side .icon{position:absolute;left:7px;top:9px}
.side .go{position:absolute;right:18px;bottom:6px;width:68px;height:19px;background:var(--navy);color:#fff;font-size:9px;font-weight:500;text-align:center;line-height:19px;border-radius:3px}
.signup .email{position:absolute;left:10px;top:79px;width:225px;height:30px;border:1px solid #ccc;border-radius:3px;background:#fff;font-size:10.5px;font-style:italic;color:#888;padding:8px 9px}
.signup .email span{position:absolute;right:-1px;top:-1px;width:37px;height:30px;background:var(--navy);color:#fff;font-style:normal;text-align:center;line-height:30px;border-radius:0 3px 3px 0;font-size:11px}
.connect h3{left:13px;top:9px}
.social{position:absolute;display:flex;align-items:center;gap:9px;font-size:11px;color:#222}
.social i{width:18px;height:18px;border-radius:2px}
.divider{position:absolute;left:266px;top:472px;width:1px;height:545px;background:var(--line)}
.main{position:absolute;left:283px;top:472px;width:525px}
.main h1{font-weight:400;color:var(--navy);font-size:20px;margin-bottom:6px}
.main p{font-size:10.6px;line-height:17.2px;margin-bottom:7px}
.main h2{font-weight:500;color:var(--navy);font-size:15px;margin:2px 0 4px}
.benefits{list-style:none}
.benefits li{height:26.8px;display:flex;align-items:center;gap:10px;font-size:10.6px}
.benefits li i{width:11px;height:11px;border-radius:2px;background:var(--sky);flex:none}
.main .cta{font-weight:500;color:var(--navy);font-size:11.2px;line-height:17px}
.main .cta b{color:var(--ink);font-weight:500}
.callband{position:absolute;left:0;top:1031px;width:823px;height:37px;background:var(--navy);color:#fff;font-size:21px;display:flex;align-items:center;justify-content:center;gap:16px}
.footlinks{position:absolute;left:0;top:1077px;width:823px;text-align:center;font-size:10.6px;color:#222;word-spacing:2px}
.copy{position:absolute;left:0;top:1099px;width:823px;text-align:center;font-size:10.6px;line-height:17px;color:#222}
.copy b{font-weight:400;color:var(--blue)}
</style>
</head>
<body>
<div class="topband">
  <div class="toplinks"><span>FAQ</span>|<span>Support</span>|<span>Log In</span>|<span><i class="chat-dot"></i>Live Chat</span></div>
</div>

<div class="sheet">
  <div class="brand">KERNEL<small>GROUP</small></div>
  <div class="search">Search Keyword..<span class="btn"></span></div>
  <div class="callus">
    <svg width="18" height="18" viewBox="0 0 18 18"><rect width="18" height="18" rx="3" fill="#333"/><path d="M6 4c-1 1-1 3 1 6s4 4 5 4l1-2-2-1-1 1c-1-1-2-2-2-3l1-1-1-2z" fill="#fff"/></svg>
    Call Us: <b>+971 4 555 0187</b>
  </div>

  <nav class="nav">
    <a>HOME</a><a>ABOUT US</a><a>SERVICES</a><a>METHODOLOGY</a><a>HOW IT WORKS</a><a>PRICING</a><a>FAQ</a><a>CONTACT US</a>
  </nav>

  <div class="hero" role="img" aria-label="Photo of smiling call center agents wearing headsets">
    <div class="trial">
      <h2>14 DAY TRIAL</h2>
      <div class="field">Name</div>
      <div class="field">Contact No.</div>
      <div class="field">Email Address</div>
      <div class="go">GET STARTED</div>
    </div>
    <div class="dots"><i></i><i></i><i></i><i></i><i></i></div>
  </div>

  <div class="side" style="top:474px;height:122px">
    <svg class="icon" width="34" height="30" viewBox="0 0 34 30"><path d="M3 10h6l8-7v24l-8-7H3z" fill="#111"/><path d="M21 9q4 6 0 12M25 5q7 10 0 20" stroke="#111" stroke-width="2.5" fill="none"/></svg>
    <h3>Listen</h3>
    <p>Kernel Telecom takes pride in ensuring that your calls are handled in the most professional manner.</p>
    <div class="go">GO</div>
  </div>

  <div class="side" style="top:612px;height:122px">
    <svg class="icon" width="34" height="36" viewBox="0 0 34 36"><text x="2" y="27" font-family="Ubuntu,sans-serif" font-size="30" font-weight="500" fill="#2d9a2a">$</text></svg>
    <h3>Request</h3>
    <p>Our prices are based on the actual agent talk time and the duration for which the services are availed.</p>
    <div class="go">GO</div>
  </div>

  <div class="side signup" style="top:752px;height:122px">
    <svg class="icon" width="38" height="38" viewBox="0 0 38 38"><rect x="2" y="12" width="34" height="24" rx="2" fill="#f39a1e"/><path d="M2 14l17 12 17-12" stroke="#fff" stroke-width="1.5" fill="none"/><path d="M4 12l15-10 15 10" fill="#f7b64a"/></svg>
    <h3>Sign Up</h3>
    <p>Sign up for our FREE Monthly Newsletter</p>
    <div class="email">Enter Email<span>GO</span></div>
  </div>

  <div class="side connect" style="top:891px;height:122px">
    <h3>Keep Your Connected</h3>
    <div class="social" style="left:14px;top:45px"><i style="background:#3b5a9a"></i>Circlebook</div>
    <div class="social" style="left:111px;top:45px"><i style="background:#1c7fbd"></i>Worknet</div>
    <div class="social" style="left:14px;top:78px"><i style="background:#4fc0e8"></i>Chirper</div>
    <div class="social" style="left:111px;top:78px"><i style="background:#333"></i>Searchly +</div>
  </div>

  <div class="divider"></div>

  <div class="main">
    <h1>Welcome to Kernel Group</h1>
    <p>Kernel Telecom is a24/7 call center and live answering service, we provide customized solutions for small, medium, and large organizations. Our customized solutions help our clients get the maximum return on their investment by capturing more leads and projecting a professional image to their customers, in addition tohuge savings on overhead and labor costs.</p>
    <h2>10 Ways Your Company Can Benefit:</h2>
    <ul class="benefits">
      <li><i></i>Capture more business &amp; increase profits.</li>
      <li><i></i>Save thousands on labor costs.</li>
      <li><i></i>Improve your company's "phone image".</li>
      <li><i></i>Streamline your call flow.</li>
      <li><i></i>Conduct business 24/7 without the overhead.</li>
      <li><i></i>Take advantage of a turn-key, streamlined solution.</li>
      <li><i></i>Respond instantaneously to clients and prospects.</li>
      <li><i></i>Kernel Telecom uses the most reliable equipment in the industry.</li>
      <li><i></i>Kernel Telecom selects the right people with the best voices.</li>
      <li><i></i>Kernel Telecom over-staffs receptionists to minimize hold times.</li>
    </ul>
    <p>At Kernel Telecom, we customize our services to each client's specific needs. We do not provide a "one size fits all" solutions. We take pride in developing solutions to fit the specific requirements of our clients' individual situation and needs.</p>
    <p>We employ the right people with the best voices and over-staff our team of live receptionists to minimize hold times. Our team of experts has experience spanning decades and cutting across industries to provide our customers with the right solution for their niche area of operation.</p>
    <div class="cta">For more information or to speak with an account specialist, please call Kernel Telecom<br>at <b>+9714-555-0187!</b></div>
  </div>

  <div class="callband">
    <svg width="22" height="22" viewBox="0 0 18 18"><rect width="18" height="18" rx="3" fill="#fff"/><path d="M6 4c-1 1-1 3 1 6s4 4 5 4l1-2-2-1-1 1c-1-1-2-2-2-3l1-1-1-2z" fill="#003a5c"/></svg>
    Call +9714-555-0187 for more information
  </div>
  <div class="footlinks">Home &nbsp;| &nbsp;About the Group &nbsp;| &nbsp;Divisions &nbsp;| &nbsp;Group Companies &nbsp;| &nbsp;Press Room &nbsp;| &nbsp;Employment &amp; Association &nbsp;| &nbsp;Contact Us</div>
  <div class="copy">Copyright © 2013 <b>Kernel Group.</b><br>All right reserved.</div>
</div>
</body>
</html>
```